Car rental website design for a UAE car rental company

This project is about creating a new website design for a car rental company located in Dubai (United Arab Emirates), I opened the same project a few months ago but I didn't receive a lot of appealing entries so I closed it but this time I am marking the project as guaranteed to avoid such situation again, if you have already provided a design before then please re-submit again on this project so that it is considered while reviewing all the designs

A few important things:

1- We need a simple non-complex design
2- The final deliverable would be 2 screens (PSD, JPEG ... etc), the first screen is for the home page and the second screen is for an internal page
3- The home page must have a section that end users can use to rent a car online directly from the home page instead of going into some inner pages
4- The current website is very old and not very appealing so avoid creating a similar design (www.quarvin-drive.example)
5- The name is Quarvin but the company rents normal cars (no Limousin cars will be rented) so avoid adding any fancy cars in the images/graphics used in the design, just normal end users cars
6- The expected pages would be: home, About us, Our team, Strategy, Contact us and links to social media pages
7- The attachments include the company's logo and some screens from other car rental companies that provide online rentals/payments

If you have any questions please feel free to ask and please note that we will need the designs urgently

Thanks

Target Market(s)

Dubai - United Arab Emirates

Industry/Entity Type

It Company

Number of Pages Required

2 page

Font styles to use
Sans Serif

Requirements
Must have
• Check the project details
Nice to have
Should not have

```html
<!DOCTYPE html>
<html lang="en">
<head>
<meta charset="utf-8">
<title>Quarvin – Rent A Car</title>
<link href="https://fonts.googleapis.com/css2?family=Arimo:wght@400;700&display=swap" rel="stylesheet">
<style>
:root{
  --brand:#a50034;
  --brand-dark:#8f002c;
  --ink:#222;
  --muted:#8a8a8a;
  --white:#fff;
  --hero-a:#3a2620;
  --hero-b:#1c1412;
}
*{margin:0;padding:0;box-sizing:border-box}
html,body{width:1009px;height:1200px;overflow:hidden;background:var(--white)}
body{position:relative;font-family:"Arimo",Arial,sans-serif;color:var(--ink)}
.abs{position:absolute}
.top-rule{left:50px;top:0;width:909px;height:2px;background:var(--brand)}
.brand{left:61px;top:15px;width:80px;height:58px;text-align:center}
.brand-mark{display:block;margin:0 auto;width:30px;height:30px;background:var(--brand)}
.brand-name{display:block;margin-top:4px;font-size:15px;color:var(--muted)}
.nav{top:35px;font-size:11.5px;letter-spacing:1.2px;color:#333}
.nav.active{color:var(--brand)}
.hero{left:0;top:86px;width:1009px;height:317px;background:radial-gradient(ellipse at 50% 45%,#4d332a 0%,var(--hero-a) 40%,var(--hero-b) 100%)}
.hero-title{left:0;top:212px;width:1009px;text-align:center;color:var(--white);font-size:27px;letter-spacing:.5px}
.hero-sub{left:0;top:258px;width:1009px;text-align:center;color:var(--white);font-size:13.5px;letter-spacing:.3px}
.welcome{left:0;top:441px;width:1009px;text-align:center;color:var(--brand);font-size:27px;letter-spacing:.5px}
.intro{left:0;top:497px;width:1009px;text-align:center;font-size:12px;line-height:16px;color:#333}
.booking{left:62px;top:582px;width:431px;height:485px;background:var(--brand);color:var(--white)}
.booking .title{left:54px;top:22px;font-size:18.5px}
.booking .car-icon{left:23px;top:26px}
.booking .label{font-size:12px}
.field{background:var(--white);color:#333;font-size:12px;height:31px;line-height:31px;padding-left:12px}
.field svg{position:absolute;top:9px;right:12px}
.booking .link{font-size:12px;text-decoration:underline}
.check{width:9px;height:9px;background:var(--white)}
.divider{left:24px;top:380px;width:383px;height:1px;background:rgba(255,255,255,.45)}
.offer-head{left:570px;top:601px;font-size:18.5px;color:var(--ink)}
.offer-title{font-size:13.5px;color:var(--ink)}
.offer-price{font-size:13.5px;color:var(--brand)}
.car-photo{border-radius:50%/40%}
.footer{left:0;top:1144px;width:1009px;height:56px;background:var(--brand)}
.copy{left:62px;top:20px;color:var(--white);font-size:13.5px}
.social{top:21px;width:14px;height:14px;border-radius:50%;background:var(--white)}
</style>
</head>
<body>
<div class="abs top-rule"></div>

<div class="abs brand"><span class="brand-mark"></span><span class="brand-name">Quarvin</span></div>
<div class="abs nav active" style="left:641px">HOME</div>
<div class="abs nav" style="left:696px">ABOUT</div>
<div class="abs nav" style="left:758px">TEAM</div>
<div class="abs nav" style="left:811px">STRATEGY</div>
<div class="abs nav" style="left:894px">CONTACT</div>

<div class="abs hero" role="img" aria-label="Dim interior view of a car with two people in the front seats"></div>
<div class="abs hero-title">EXPRERIENCE AN EXTRA MILE</div>
<div class="abs hero-sub">OF COMFORT, PLEASURE AND LEISURE FROM THE BEST</div>

<div class="abs welcome">WELCOME TO QUARVIN</div>
<div class="abs intro">As Dubai is expected to welcome millions of tourists and visitors, car rental industry is believed to escalate more rapidly in the region.<br>Over the past five years, demands for car rentals in Dubai has been augmenting at a healthy pace<br>and is currently registering a growth rate of 20 to 25 percent per year.</div>

<section class="abs booking">
  <svg class="abs car-icon" width="20" height="16" viewBox="0 0 20 16"><path d="M3 7l2-5h10l2 5h1v6h-2v2h-3v-2H7v2H4v-2H2V7z" fill="#fff"/><circle cx="5.5" cy="10" r="1.3" fill="#a50034"/><circle cx="14.5" cy="10" r="1.3" fill="#a50034"/><path d="M6 3h8l1.4 4H4.6z" fill="#a50034"/></svg>
  <div class="abs title">BOOK A CAR</div>
  <div class="abs label" style="left:23px;top:82px">1. Pick-up Location &nbsp;&nbsp;&nbsp;(City, State, Airport Code)</div>
  <div class="abs field" style="left:23px;top:109px;width:234px">Dubai Airport - Terminal 3</div>
  <div class="abs link" style="left:23px;top:152px">Help me find a rental location.</div>
  <div class="abs check" style="left:24px;top:180px"></div>
  <div class="abs label" style="left:45px;top:176px;font-weight:700;font-size:12px">Return car to a different location</div>
  <div class="abs label" style="left:23px;top:215px">2. Pick-up Date and Time</div>
  <div class="abs field" style="left:24px;top:243px;width:173px">01 / 05 / 2015
    <svg width="17" height="15" viewBox="0 0 17 15"><rect x=".5" y="2" width="16" height="12.5" fill="none" stroke="#333"/><rect x=".5" y="2" width="16" height="3" fill="#333"/><g fill="#333"><rect x="3" y="7" width="2" height="2"/><rect x="7" y="7" width="2" height="2"/><rect x="11" y="7" width="2" height="2"/><rect x="3" y="10.5" width="2" height="2"/><rect x="7" y="10.5" width="2" height="2"/><rect x="11" y="10.5" width="2" height="2"/></g></svg></div>
  <div class="abs field" style="left:236px;top:243px;width:119px">12 : 00 p.m.
    <svg width="18" height="10" viewBox="0 0 18 10"><path d="M0 0h18L9 10z" fill="#111"/></svg></div>
  <div class="abs label" style="left:24px;top:297px">Return Date and Time</div>
  <div class="abs field" style="left:24px;top:325px;width:173px">10 / 05 / 2015
    <svg width="17" height="15" viewBox="0 0 17 15"><rect x=".5" y="2" width="16" height="12.5" fill="none" stroke="#333"/><rect x=".5" y="2" width="16" height="3" fill="#333"/><g fill="#333"><rect x="3" y="7" width="2" height="2"/><rect x="7" y="7" width="2" height="2"/><rect x="11" y="7" width="2" height="2"/><rect x="3" y="10.5" width="2" height="2"/><rect x="7" y="10.5" width="2" height="2"/><rect x="11" y="10.5" width="2" height="2"/></g></svg></div>
  <div class="abs field" style="left:236px;top:325px;width:119px">12 : 00 p.m.
    <svg width="18" height="10" viewBox="0 0 18 10"><path d="M0 0h18L9 10z" fill="#111"/></svg></div>
  <div class="abs divider"></div>
  <div class="abs label" style="left:23px;top:403px">Hire Car Type</div>
  <div class="abs field" style="left:23px;top:430px;width:233px">Automatic
    <svg width="18" height="10" viewBox="0 0 18 10"><path d="M0 0h18L9 10z" fill="#111"/></svg></div>
</section>

<svg class="abs" style="left:539px;top:603px" width="19" height="19" viewBox="0 0 19 19"><circle cx="9.5" cy="9.5" r="8.5" fill="none" stroke="#222" stroke-width="1.6"/><circle cx="9.5" cy="9.5" r="5" fill="#222"/></svg>
<div class="abs offer-head">LATEST OFFER</div>

<div class="abs offer-title" style="left:540px;top:647px">2015 Red Car Lorem Ipsum 1.9</div>
<div class="abs offer-price" style="left:540px;top:675px">AED 2.099 Per Month</div>
<div class="abs car-photo" style="left:560px;top:690px;width:380px;height:140px;background:radial-gradient(ellipse at 55% 50%,#c8202a 0%,#b5252c 35%,rgba(200,200,200,.4) 65%,rgba(255,255,255,0) 80%)" role="img" aria-label="Red compact coupe, side three-quarter view"></div>

<div class="abs offer-title" style="left:536px;top:878px">2015 Red Car Lorem Ipsum 2.0</div>
<div class="abs offer-price" style="left:536px;top:906px">AED 3.099 Per Month</div>
<div class="abs car-photo" style="left:746px;top:876px;width:196px;height:154px;background:radial-gradient(ellipse at 50% 50%,#d42a30 0%,#b81f27 45%,rgba(200,200,200,.35) 70%,rgba(255,255,255,0) 82%)" role="img" aria-label="Red hatchback, front view"></div>

<footer class="abs footer">
  <div class="abs copy">2015 © Quarvin</div>
  <span class="abs social" style="left:806px"></span>
  <span class="abs social" style="left:828px"></span>
  <span class="abs social" style="left:855px"></span>
  <span class="abs social" style="left:879px"></span>
  <span class="abs social" style="left:903px"></span>
  <svg class="abs" style="left:928px;top:21px" width="20" height="14" viewBox="0 0 20 14"><rect x=".8" y=".8" width="18.4" height="12.4" fill="none" stroke="#fff" stroke-width="1.6"/><path d="M1 1l9 7 9-7M1 13l6.5-6M19 13l-6.5-6" fill="none" stroke="#fff" stroke-width="1.4"/></svg>
</footer>
</body>
</html>
```